New Business Card Design for Manufacturing

We are an engineering/manufacturing company that offers Advanced machining/assembly/engineering services, as well as innovative products for the heavy duty engine cooling markets.

We are looking to get a new business card designed that is clean and modern looking, but still fits the wide range of technical/skilled work we do.

- We hope to use this design as the base for other design work in new Presentations, web, and print work.

Industry/Entity Type

Engineering

Contact Information for Business Card

Our preferred color of blue is (RGB) 22/71/159 but can vary slightly from that color. Our content will be our Logo and full company name (Corvath Tooling Works, Inc.), company address, name, job title, phone number with extension, cell number, fax number, website, and email address on the cards.
We'd like the full company name next to the logo, but we are open to other interpretations of that layout.
Preferably, we would like the back side to be clean with just our logo, and the front to contain all of the contact information.

Colors
2f74b4
0355a3
85abd2

Requirements
Must have
• - Logo, company name, needed content - We are open to interpretation beyond that.
• - Standard size business card.
• - Horizontal orientation.
• - Enough space for lengthy names / job titles (for example, a job title could read "Directory of Human Resources" or "V.P. of Governmental Affairs"). We need this to look clean, whether the title be short (CEO) or long (as described above).

```html
<!DOCTYPE html>
<html lang="en">
<head>
<meta charset="utf-8">
<title>Corvath Tooling Works – Business Card</title>
<link href="https://fonts.googleapis.com/css2?family=Fira+Sans:wght@400;500;700;800&display=swap" rel="stylesheet">
<style>
  :root {
    --brand-blue: #16479f;
    --ink: #2b2b2b;
    --muted-grey: #8a8a8a;
    --card-black: #0b0b0c;
    --card-white: #f7f7f7;
    --backdrop: #e2e2e2;
    --wordmark-white: #f2f2f2;
  }
  * { box-sizing: border-box; margin: 0; padding: 0; }
  html, body {
    width: 1200px; height: 576px; overflow: hidden;
    background: var(--backdrop);
    font-family: "Fira Sans", Arial, sans-serif;
  }
  .canvas { position: relative; width: 1200px; height: 576px; }

  .card {
    position: absolute; top: 138px; height: 293px; border-radius: 13px;
    box-shadow: 0 4px 10px rgba(0,0,0,0.25);
    overflow: hidden;
  }
  .card--back { left: 82px; width: 484px; background: var(--card-black); }
  .card--front { left: 602px; width: 481px; background: var(--card-white); }

  /* Back: logo only */
  .back-lockup { position: absolute; left: 96px; top: 100px; }
  .wordmark {
    display: flex; align-items: center; gap: 10px;
    font-weight: 800; letter-spacing: 1px; line-height: 1;
  }
  .wordmark__square { display: block; background: var(--brand-blue); }
  .back-lockup .wordmark { font-size: 60px; color: var(--wordmark-white); }
  .back-lockup .wordmark__square { width: 30px; height: 30px; }
  .tagline {
    font-weight: 700; text-transform: uppercase; color: var(--muted-grey);
    letter-spacing: 0.5px;
  }
  .back-lockup .tagline { font-size: 19px; margin-top: 10px; }

  /* Front */
  .front-lockup { position: absolute; left: 30px; top: 110px; }
  .front-lockup .wordmark { font-size: 36px; color: var(--brand-blue); gap: 7px; }
  .front-lockup .wordmark__square { width: 18px; height: 18px; }
  .front-lockup .tagline { font-size: 12px; margin-top: 6px; }

  .contact-block { position: absolute; left: 270px; top: 46px; color: var(--ink); }
  .person-name { font-size: 21px; font-weight: 500; color: var(--brand-blue); line-height: 1.1; }
  .person-title { font-size: 12px; margin-top: 3px; }
  .contact-list { list-style: none; margin-top: 15px; }
  .contact-list li {
    display: flex; align-items: center; gap: 8px;
    font-size: 13px; height: 17.5px; white-space: nowrap;
  }
  .contact-list svg { width: 10px; height: 10px; fill: var(--brand-blue); flex: none; }
  .address { font-size: 13px; line-height: 17px; margin-top: 8px; }

  .front-rule {
    position: absolute; left: 22px; right: 22px; top: 256px;
    border-top: 1.5px solid var(--brand-blue);
  }
  .company-name {
    position: absolute; left: 0; right: 0; top: 265px; text-align: center;
    font-size: 13.5px; font-weight: 500; color: var(--brand-blue);
  }
</style>
</head>
<body>
<main class="canvas">

  <section class="card card--back" aria-label="Card back">
    <div class="back-lockup">
      <div class="wordmark"><span class="wordmark__square"></span>CORVATH</div>
      <div class="tagline">Built to Run</div>
    </div>
  </section>

  <section class="card card--front" aria-label="Card front">
    <div class="front-lockup">
      <div class="wordmark"><span class="wordmark__square"></span>CORVATH</div>
      <div class="tagline">Built to Run</div>
    </div>

    <div class="contact-block">
      <h1 class="person-name">John Doe Smith</h1>
      <p class="person-title">Managing Director</p>
      <ul class="contact-list">
        <li><svg viewBox="0 0 10 10"><path d="M1 3.5 Q5 0 9 3.5 L8 5 L6.5 4 L6.5 3 Q5 2.6 3.5 3 L3.5 4 L2 5 Z M2.5 6 H7.5 V9 H2.5 Z"/></svg>111-2222-2222 (Ext. 104)</li>
        <li><svg viewBox="0 0 10 10"><path d="M2.5 0.5 H7.5 V9.5 H2.5 Z M3.3 1.5 V7.5 H6.7 V1.5 Z"/></svg>333-3333-3333</li>
        <li><svg viewBox="0 0 10 10"><path d="M2.5 0.5 H7.5 V3 H2.5 Z M0.5 3.5 H9.5 V7.5 H8 V6 H2 V7.5 H0.5 Z M2.5 6.5 H7.5 V9.5 H2.5 Z"/></svg>444-4444-4444</li>
        <li><svg viewBox="0 0 10 10"><path d="M0.5 2 H9.5 V8 H0.5 Z M1 2.5 L5 5.5 L9 2.5 L9 3.2 L5 6.2 L1 3.2 Z" fill-rule="evenodd"/></svg>www.yourwebsite.com</li>
        <li><svg viewBox="0 0 10 10"><circle cx="5" cy="5" r="4.5"/><path d="M0.5 5 H9.5 M5 0.5 V9.5" stroke="#f7f7f7" stroke-width="0.8"/></svg>johndoe@yourwebsite.com</li>
      </ul>
      <p class="address">234 Anywhere St., Any City,<br>Any Town, US 123456</p>
    </div>

    <div class="front-rule"></div>
    <p class="company-name">Corvath Tooling Works, Inc.</p>
  </section>

</main>
</body>
</html>
```